Website Design - for Energy Efficiency company - large corporate feel

Hi there,
Thanks for checking out this project!
We're a UK based energy efficiency business. We arrange for energy efficient systems to be fitted in people's houses (i.e. efficient boilers, solar panels etc.) However, we do not install them ourselves as we have accredited installers who install on our behalf. Therefore the website should appeal to these businesses and have a very professional corporate feel. The final design should communicate that we are a financially safe large corporation.
Our existing website should not be used for inspiration as the style and content are very outdated (it was from a time when were installers - which we no longer are).
The new website design should use the greens from our logo, however I don't want the site saturated in this colour.
I'm really open to your chosen layout and therefore I'm not a huge fan of including links to websites I like - as I don't want to limit your own creativity. However, I would like it to look corporate (but not too boring and unimaginative).
So here's a few links to websites that I feel give a feel of financially safe / large corporate etc. Although you certainly don't have to design with this style / layout in mind:
http://www.brelvanhub.org.uk/advice
http://www.tolvenrise.co.uk/
http://www.qpwd.org.uk/
http://www.wendrowkeyplot.co.uk/
http://www.ruvasto.co.uk/ (very bad design but looks corporate)
http://www.pellarwatt.org.uk/
http://www.vq.co.uk/ (looks corporate but too busy and boring)
http://www.quellisto.co.uk/business/index.htm
http://www.dormavel.com/
https://www.ostrevan.com/en/index.html
The site is for 4 different audiences:
Consumers | Businesses | Public Sector | Installers
Therefore, it's important that there is some form of way of splitting the site up into these sections (almost like 4 websites in 1). Each section will then have the navigation menu with 7 links.
I've attached our logo (company-logo.jpg) and another logo design we have to display inline with regulations (blue-pact-logo.jpg).
Happy designing, and thank you!

```html
<!DOCTYPE html>
<html lang="en">
<head>
<meta charset="utf-8">
<title>Leafhold Energy</title>
<link href="https://fonts.googleapis.com/css2?family=Open+Sans:ital,wght@0,300;0,400;0,600;0,700;0,800;1,300&display=swap" rel="stylesheet">
<style>
:root{
  --green:#4e7f22;
  --green-dark:#2f4d12;
  --green-light:#8cc63e;
  --green-btn:#8bc53f;
  --ink:#222b2c;
  --text:#3a3a3a;
  --grey-band:#e7e7e7;
  --grey-card:#f1f1f1;
  --grey-btn:#4d4d4d;
  --white:#fff;
}
*{margin:0;padding:0;box-sizing:border-box}
html,body{width:933px;height:1200px;overflow:hidden;background:var(--white)}
body{position:relative;font-family:"Open Sans",Arial,sans-serif;color:var(--text)}
.abs{position:absolute}
.top-rule{left:0;top:0;width:933px;height:3px;background:var(--green-light)}
.brand{left:140px;top:26px;display:flex;align-items:center;gap:8px}
.brand-dot{width:36px;height:36px;border-radius:50%;background:var(--green)}
.brand-name{font-size:27px;font-weight:600;color:var(--green);letter-spacing:.5px}
.approval-badge{left:714px;top:10px;width:60px;height:66px;background:var(--green);border-radius:3px}
.main-nav{left:0;top:83px;width:933px;height:29px;background:var(--green);border-bottom:3px solid var(--green-light);box-sizing:content-box}
.main-nav ul{position:absolute;left:140px;top:0;display:flex;list-style:none;height:29px}
.main-nav li{height:29px;line-height:29px;text-align:center;color:var(--white);font-size:13.5px;border-right:1px solid rgba(255,255,255,.35)}
.main-nav li:last-child{border-right:none}
.main-nav li.active{background:var(--green-light)}
.hero{left:0;top:115px;width:933px;height:240px;background:linear-gradient(90deg,#7fa5a3 0%,#b9d0ce 45%,#c6d9d7 65%,#8fb2b0 100%)}
.hero-title{left:140px;top:142px;font-size:46px;font-weight:800;color:var(--ink);letter-spacing:.5px}
.hero-sub{left:140px;top:192px;font-size:34px;font-weight:300;color:var(--ink);line-height:40px}
.hero-sub em{font-style:italic}
.hero-product{left:620px;top:124px;width:150px;height:222px;background:linear-gradient(90deg,#cfd6d6,#f1f3f3 50%,#d6dbdb);border-radius:4px}
.hero-dots{left:150px;top:333px;display:flex;gap:11px}
.hero-dots span{width:11px;height:11px;border-radius:50%;background:#a9c3c1}
.hero-dots span.on{background:#fff}
.hero-rule{left:0;top:355px;width:933px;height:3px;background:var(--green)}
.quote-band{left:0;top:358px;width:933px;height:75px;background:var(--grey-band)}
.quote-text{left:151px;top:365px;font-size:20.5px;line-height:30px;color:#222}
.quote-btn{left:632px;top:374px;width:161px;height:37px;border-radius:4px;background:linear-gradient(#9ed14f,#76b12c);color:#fff;font-weight:700;font-size:14.5px;text-align:center;line-height:37px;box-shadow:0 2px 2px rgba(0,0,0,.2)}
.audience{top:445px;width:154px;height:141px;border:1px solid #dcdcdc;background:linear-gradient(#fff,#ebebeb);text-align:center}
.audience.active{background:var(--green);border-color:var(--green)}
.audience svg{position:absolute;left:57px;top:10px}
.audience h2{position:absolute;left:0;right:0;top:59px;font-size:25px;font-weight:300;color:#333}
.audience.active h2{color:#fff}
.call-btn{position:absolute;left:20px;top:105px;width:114px;height:26px;background:var(--grey-btn);color:#fff;font-size:11.5px;font-weight:700;line-height:26px;border-radius:2px}
.audience.active .call-btn{background:#fff;color:var(--green)}
.call-btn b{font-size:14px;margin-left:5px}
.intro{left:140px;top:609px;width:479px;font-size:9.4px;line-height:13.5px;text-align:justify}
.intro p{margin-bottom:14px}
.intro-photo{left:633px;top:613px;width:161px;height:155px;background:linear-gradient(#7a7d78,#4c5e78 60%,#3c4d6c)}
.section-title{top:823px;font-size:21px;font-weight:400;color:#222;display:flex;align-items:center}
.section-title::after{content:"";display:block;height:3px;background:#e6e6e6;margin-left:8px}
.news-title::after{width:258px}
.say-title::after{width:160px}
.news-item{left:140px;width:320px}
.date{position:absolute;left:0;top:0;width:47px}
.date .day{height:31px;background:#e1e1e1;text-align:center;font-size:21px;font-weight:700;color:#333;line-height:31px}
.date .mon{height:18px;background:var(--green);color:#fff;text-align:center;font-size:10px;line-height:18px}
.news-item h3{position:absolute;left:54px;top:-3px;font-size:13.5px;font-weight:400;color:#222}
.news-item p{position:absolute;left:54px;top:18px;width:266px;font-size:9.3px;line-height:13px;text-align:justify}
.testimonial{left:473px;top:862px;width:321px;height:78px;background:#f1f1f1}
.testimonial .mark{position:absolute;left:10px;top:4px;font-size:34px;color:#bbb;font-style:italic}
.testimonial p{position:absolute;left:38px;top:19px;width:272px;font-size:9.3px;line-height:13px;text-align:justify}
.testimonial-tail{left:767px;top:940px;width:0;height:0;border-left:8px solid transparent;border-right:8px solid transparent;border-top:8px solid #f1f1f1}
.author{left:631px;top:985px;font-size:10px;color:#555}
.author strong{font-size:12.5px;font-style:italic;color:var(--green);font-weight:600}
.avatar{left:740px;top:958px;width:56px;height:56px;border-radius:50%;background:linear-gradient(#e79fbd,#e9c3a0)}
.contact-band{left:0;top:1027px;width:933px;height:54px;background:var(--grey-band)}
.contact-item{top:1034px;display:flex;align-items:center;gap:10px;font-size:15px;color:#222}
.band-divider{left:645px;top:1027px;width:2px;height:54px;background:#fff}
.support{left:667px;top:1041px;font-size:10.5px;line-height:12px;text-align:center;color:#333}
.support-hours{left:728px;top:1030px;font-size:25px;font-weight:800;line-height:24px;color:var(--green-dark);text-align:center}
.site-footer{left:0;top:1081px;width:933px;height:89px;background:var(--green)}
.footer-links{top:1093px;list-style:none;font-size:9.5px;color:#fff;line-height:20px;font-weight:600}
.newsletter-label{left:396px;top:1089px;font-size:12.5px;color:#fff}
.newsletter-input{left:395px;top:1125px;width:166px;height:25px;background:#fff;border-radius:3px}
.footer-note{left:724px;top:1093px;width:90px;font-size:10.5px;font-weight:600;line-height:14.5px;color:#fff}
.bottom-bar{left:0;top:1170px;width:933px;height:30px;background:var(--green-dark)}
.copyright{left:140px;top:1177px;font-size:8.5px;color:#a9b89c}
.social{top:1177px;width:16px;height:16px;border-radius:2px}
</style>
</head>
<body>
<div class="abs top-rule"></div>
<div class="abs brand"><span class="brand-dot"></span><span class="brand-name">Leafhold Energy</span></div>
<div class="abs approval-badge" role="img" aria-label="Regulatory approval badge"></div>

<nav class="abs main-nav">
  <ul>
    <li class="active" style="width:63px">Home</li>
    <li style="width:91px">About Us</li>
    <li style="width:111px">Blue Pact</li>
    <li style="width:68px">ECO</li>
    <li style="width:108px">Landlords</li>
    <li style="width:117px">Renewables</li>
    <li style="width:95px">Contact Us</li>
  </ul>
</nav>

<section class="abs hero"></section>
<div class="abs hero-title">FREE BOILER</div>
<div class="abs hero-sub">Installed under the<br><em>'ECO Scheme'</em></div>
<div class="abs hero-product" role="img" aria-label="Wall-mounted combination boiler"></div>
<div class="abs hero-dots"><span class="on"></span><span></span><span></span></div>
<div class="abs hero-rule"></div>

<div class="abs quote-band"></div>
<div class="abs quote-text">Lorem ipsum dolor sit amet, conm soretectetuer<br>Aenean massa. Cum sociis naeryyubttoquetr ert</div>
<div class="abs quote-btn">GET A FREE QUOTE</div>

<div class="abs audience active" style="left:140px">
  <svg width="40" height="42" viewBox="0 0 40 42"><circle cx="20" cy="9" r="8" fill="#fff"/><path d="M4 42V26q0-7 7-7h18q7 0 7 7v16z" fill="#fff"/><path d="M18 19h4l1 4-3 14-3-14z" fill="#4e7f22"/></svg>
  <h2>Consumers</h2>
  <div class="call-btn">CALL US NOW<b>›</b></div>
</div>
<div class="abs audience" style="left:306px">
  <svg width="42" height="42" viewBox="0 0 42 42"><g fill="#444"><circle cx="21" cy="6" r="4"/><path d="M5 14h32l3 20H2z"/><rect x="19" y="34" width="4" height="5"/><rect x="11" y="38" width="20" height="3"/></g><g stroke="#fff" stroke-width="1.3"><path d="M4 21h34M3 27h36M13 14l-1 20M21 14v20M29 14l1 20"/></g></svg>
  <h2>Businesses</h2>
  <div class="call-btn">CALL US NOW<b>›</b></div>
</div>
<div class="abs audience" style="left:473px">
  <svg width="42" height="44" viewBox="0 0 42 44"><circle cx="17" cy="17" r="14" fill="none" stroke="#444" stroke-width="3"/><circle cx="17" cy="17" r="7" fill="none" stroke="#444" stroke-width="3"/><path d="M16 16l22 10-9 3 7 9-4 3-7-9-5 8z" fill="#444" stroke="#fff" stroke-width="1.5"/></svg>
  <h2>Public Sector</h2>
  <div class="call-btn">CALL US NOW<b>›</b></div>
</div>
<div class="abs audience" style="left:640px">
  <svg width="42" height="42" viewBox="0 0 42 42"><g fill="#444"><path d="M6 36l22-22 4 4-22 22-4 0z"/><path d="M26 4a9 9 0 0 1 11 11l-5-1-2-2-1-5z"/><path d="M4 8l6-4 26 26 -4 6z"/></g></svg>
  <h2>Installers</h2>
  <div class="call-btn">CALL US NOW<b>›</b></div>
</div>

<div class="abs intro">
  <p>Lorem ipsum dolor sit amet, consectetuer adipiscing elit. Aenean commLorem ipsum dolor sit amet, consectetuer adipiscing elit. Aenean commodo ligula eget dolor. Aenean massa. Cum sociis natoLorem ipsum dolor sit amet, consectetuer adipiscing elit. Aenean commLorem ipsum dolor sit amet, consectetuer adipiscing elit. Aenean commodo ligula eget dolor. Aenean massa. Cum sociis natoque penatibus et magnis dis parturient montes, nascetur ridiculus mus. Donec quam felis, ultricies nec, pellentesque eu, pretium quis, sem.</p>
  <p>Nulla consequat massa quis enim. Donec pede justo, fringilla vel, aliquet nec,Nulla consequat massa quis enim. Donec pede justo, fringilla vel, aliquet nec, vulputate eget, arcu.odo ligula eget dolor. vulputate eget, arcu.odo ligula eget dolor. Aenean massa. Cum sociis natoque penatibus et magnis dis parturient montes, nascetur</p>
  <p>Donec pede justo, fringilla vel, aliquet nec, vulputate eget, arcu.que penatibus et magnis dis parturient montes, nascetur ridiculus mus. Donec quam felis, ultricies nec, pellentesque eu, pretium quis, sem. Nulla consequat massa quis enim. Donec pede justo,</p>
</div>
<div class="abs intro-photo" role="img" aria-label="Installer fitting solar panels on a roof"></div>

<h2 class="abs section-title news-title" style="left:140px">NEWS</h2>
<h2 class="abs section-title say-title" style="left:473px">What other’s say</h2>

<article class="abs news-item" style="top:862px">
  <div class="date"><div class="day">06</div><div class="mon">NOV</div></div>
  <h3>Lorem ipsum dolor sit amet</h3>
  <p>Lorem ipsum dolor sit amet, consectetuer adipiscing elit. Aenean commLorem ipsum dolor sit amet, consectetuer adipiscing elit. Aenean commodo ligula eget dolor. Aenean massa.</p>
</article>
<article class="abs news-item" style="top:947px">
  <div class="date"><div class="day">06</div><div class="mon">NOV</div></div>
  <h3>Lorem ipsum dolor sit amet</h3>
  <p>Lorem ipsum dolor sit amet, consectetuer adipiscing elit. Aenean commLorem ipsum dolor sit amet, consectetuer adipiscing elit. Aenean commodo ligula eget dolor. Aenean massa.</p>
</article>

<blockquote class="abs testimonial">
  <span class="mark">“</span>
  <p>Lorem ipsum dolor sit ameolor sit amet, consectetuer adipiscing elit. Aenean commodo ligula egt, consectetuer adipiscing elit. Aenean commLorem ipsum dolor sit amet, consectetuer adipiscing elit. Aenean commodo ligula eget dolor. Aenean massa.”</p>
</blockquote>
<div class="abs testimonial-tail"></div>
<div class="abs author"><strong>Marisol</strong> xyz company</div>
<div class="abs avatar" role="img" aria-label="Customer portrait"></div>

<div class="abs contact-band"></div>
<div class="abs contact-item" style="left:147px">
  <svg width="37" height="37" viewBox="0 0 37 37"><circle cx="18.5" cy="18.5" r="17" fill="none" stroke="#2f4d12" stroke-width="2"/><path d="M12 10l4-1 2 5-2 2q2 4 5 6l2-2 5 2-1 4q-3 2-8-1-6-4-8-10-1-3 1-5z" fill="#2f4d12"/></svg>
  <span>Tel: (020) 7946 0321</span>
</div>
<div class="abs contact-item" style="left:392px">
  <svg width="37" height="37" viewBox="0 0 37 37"><circle cx="18.5" cy="18.5" r="17" fill="none" stroke="#2f4d12" stroke-width="2"/><rect x="9" y="12" width="19" height="13" fill="#2f4d12"/><path d="M9 12l9.5 8 9.5-8" fill="none" stroke="#e7e7e7" stroke-width="1.5"/></svg>
  <span>Email: info@leafhold.co.uk</span>
</div>
<div class="abs band-divider"></div>
<div class="abs support">We’ve got<br>your back</div>
<div class="abs support-hours">24x7<br>365</div>

<footer class="abs site-footer"></footer>
<ul class="abs footer-links" style="left:154px"><li>Home</li><li>About Us</li><li>Blue Pact</li></ul>
<ul class="abs footer-links" style="left:248px"><li>ECO</li><li>Landlords</li><li>Renewables</li></ul>
<div class="abs newsletter-label">Newsletter</div>
<div class="abs newsletter-input"></div>
<svg class="abs" style="left:664px;top:1091px" width="44" height="42" viewBox="0 0 44 42"><path d="M22 2a9 9 0 0 1 9 9c0 7-9 17-9 17s-9-10-9-17a9 9 0 0 1 9-9z" fill="#fff"/><circle cx="22" cy="11" r="3.5" fill="#4e7f22"/><path d="M12 26l-9 14h38l-9-14" fill="none" stroke="#fff" stroke-width="2"/></svg>
<div class="abs footer-note">Lorem ipsum dolor sit amet, consectetur a dipiscing elit.</div>

<div class="abs bottom-bar"></div>
<div class="abs copyright">Copyright 2013 Leafhold</div>
<div class="abs social" style="left:705px;background:#3aa3d8"></div>
<div class="abs social" style="left:729px;background:#3b5b98"></div>
<div class="abs social" style="left:753px;background:#c8302a"></div>
<div class="abs social" style="left:777px;background:#2b77b0"></div>
</body>
</html>
```